Bright Ridge Coatings

Hi
I'm looking for a unique and eye-catching design for my business card that reflects the identity of my business. We specialize in residential, commercial, insurance, real state, heritage,and body corporate painting services and I want the card to make a memorable impression on potential clients.

Key elements to include are:
- Our logo (attached)
- Contact information: my name is darian volkema but my short name is dar, im a director of this business, number: 0457893014, email: info@brightridgecoatings.com.au
Website: www.brightridgecoatings.com.au
Social media: facebook, instagram.

I'm open to creative ideas and unconventional formats, but it's important that the design maintains a professional look.

I'd like to see some initial concepts within the few days, and I'm willing to discuss any ideas you have.

Looking forward to seeing your creativity at work!

I prefer the colours pretty much the same as my logo, but i would be happy see if my logo match with other colours.
Thanks very much

Best regards,
Dar

Our target market consists of residential exterior and interior painting, basically we do all commercial jobs, bod corporate , heritage

Residential and commercial painting

All my information as provided!! Im not sure if you guys have access to my logo through with all the format in my account??

Serif

• My business card should be double sided,
• Its nice to have all my information in front and the rest at the back, like what we we do like residential , interior exterior and as i mentioned

```html
<!DOCTYPE html>
<html lang="en">
<head>
<meta charset="UTF-8">
<title>Bright Ridge Coatings – Business Card</title>
<link href="https://fonts.googleapis.com/css2?family=Roboto+Condensed:wght@400;700&display=swap" rel="stylesheet">
<style>
  :root {
    --stage: #2a2a2b;
    --card: #222225;
    --card-pattern-light: #3a3a3e;
    --card-pattern-dark: #1c1c1f;
    --red: #b7312c;
    --blue: #3c5d9c;
    --green: #4f6b45;
    --white: #ffffff;
    --soft-white: #e9e9ec;
  }
  * { margin: 0; padding: 0; box-sizing: border-box; }
  html, body {
    width: 1200px; height: 780px; overflow: hidden;
    background: var(--stage);
    font-family: "Roboto Condensed", "Arial Narrow", sans-serif;
  }
  .stage { position: relative; width: 1200px; height: 780px; }
  .card {
    position: absolute; left: 300px; width: 600px; height: 343px;
    border-radius: 18px; background: var(--card); overflow: hidden;
    box-shadow: 0 14px 30px rgba(0,0,0,.55);
  }
  .card--back { top: 24px; }
  .card--front { top: 413px; }

  /* Back side */
  .back-texture {
    position: absolute; inset: 0;
    background: linear-gradient(115deg, var(--card-pattern-light) 0%, #2a2a2e 28%, var(--card-pattern-dark) 55%, #262629 100%);
  }
  .back-brand {
    position: absolute; top: 22px; right: 26px;
    display: flex; align-items: center; gap: 6px;
    font-size: 11px; font-weight: 700; color: var(--blue); letter-spacing: .5px;
  }
  .back-brand__mark { width: 9px; height: 9px; background: var(--red); }
  .specialties { position: absolute; left: 40px; right: 30px; bottom: 30px; }
  .specialties__title {
    color: var(--red); font-weight: 700; font-size: 15px;
    margin-left: 224px; margin-bottom: 3px; letter-spacing: .3px;
  }
  .specialties__list {
    list-style: none; display: flex; flex-wrap: nowrap;
    color: var(--white); font-size: 12.5px; white-space: nowrap;
  }
  .specialties__list li { display: flex; align-items: center; }
  .specialties__list li + li::before {
    content: ""; width: 7px; height: 7px; border-radius: 50%;
    background: var(--red); margin: 0 4px;
  }

  /* Front side */
  .front-wave { position: absolute; inset: 0; }
  .front-brand {
    position: absolute; left: 38px; top: 150px;
    display: flex; align-items: center; gap: 8px;
    font-size: 22px; font-weight: 700; color: var(--blue); letter-spacing: .6px;
  }
  .front-brand__mark { width: 16px; height: 16px; background: var(--green); }
  .divider {
    position: absolute; left: 292px; top: 80px; width: 1px; height: 150px;
    background: var(--soft-white);
  }
  .contact { position: absolute; left: 322px; top: 52px; color: var(--white); }
  .contact__name { font-size: 30px; font-weight: 700; color: var(--blue); line-height: 1; }
  .contact__nick { color: var(--red); }
  .contact__role { font-size: 15px; margin: 4px 0 14px 14px; }
  .contact__list { list-style: none; font-size: 14px; }
  .contact__list li { display: flex; align-items: center; gap: 8px; margin-bottom: 5px; }
  .contact__list svg { width: 13px; height: 13px; flex: none; }
  .social {
    position: absolute; right: 86px; bottom: 58px;
    display: flex; align-items: center; gap: 8px;
    color: var(--white); font-size: 15px;
  }
  .social__dot { width: 14px; height: 14px; border-radius: 50%; background: var(--white); }
  .social__dot--outline { background: none; border: 2px solid var(--white); border-radius: 4px; }
</style>
</head>
<body>
<main class="stage">

  <section class="card card--back" aria-label="Card back">
    <div class="back-texture" role="img" aria-label="Tonal repeating brand-mark pattern across the card"></div>
    <div class="back-brand"><span class="back-brand__mark"></span>Bright Ridge Coatings</div>
    <div class="specialties">
      <p class="specialties__title">WE SPECIALIZE</p>
      <ul class="specialties__list">
        <li>Residential</li>
        <li>Commercial</li>
        <li>Insurance</li>
        <li>Real state</li>
        <li>Heritage</li>
        <li>Body corporate painting services</li>
      </ul>
    </div>
  </section>

  <section class="card card--front" aria-label="Card front">
    <svg class="front-wave" viewBox="0 0 600 343" preserveAspectRatio="none" aria-hidden="true">
      <path d="M0,300 C170,318 300,300 400,250 C480,215 550,200 600,198 L600,343 L0,343 Z" fill="var(--red)"/>
      <path d="M150,292 C260,292 330,268 400,236 C480,202 545,188 580,186" fill="none" stroke="var(--blue)" stroke-width="5"/>
    </svg>

    <div class="front-brand"><span class="front-brand__mark"></span>Bright Ridge Coatings</div>
    <div class="divider"></div>

    <div class="contact">
      <h1 class="contact__name">Darian Volkema <span class="contact__nick">(Dar)</span></h1>
      <p class="contact__role">Director</p>
      <ul class="contact__list">
        <li>
          <svg viewBox="0 0 24 24"><path fill="var(--red)" d="M6.6 10.8a15 15 0 0 0 6.6 6.6l2.2-2.2c.3-.3.7-.4 1-.2 1.1.4 2.3.6 3.6.6.6 0 1 .4 1 1V20c0 .6-.4 1-1 1C10.6 21 3 13.4 3 4c0-.6.4-1 1-1h3.5c.6 0 1 .4 1 1 0 1.3.2 2.5.6 3.6.1.3 0 .7-.2 1z"/></svg>
          0457 893 014
        </li>
        <li>
          <svg viewBox="0 0 24 24"><circle cx="12" cy="12" r="10" fill="var(--green)"/><path d="M2 12h20M12 2c3 3 3 17 0 20M12 2c-3 3-3 17 0 20" stroke="var(--card)" stroke-width="1.4" fill="none"/></svg>
          info@brightridgecoatings.com.au
        </li>
        <li>
          <svg viewBox="0 0 24 24"><rect x="2" y="5" width="20" height="14" rx="2" fill="var(--blue)"/><path d="M3 6l9 7 9-7" stroke="var(--card)" stroke-width="1.6" fill="none"/></svg>
          www.brightridgecoatings.com.au
        </li>
      </ul>
    </div>

    <div class="social">
      <span>Follow us</span>
      <span class="social__dot"></span>
      <span class="social__dot social__dot--outline"></span>
    </div>
  </section>

</main>
</body>
</html>
```